Artist needs a business card for her pencil portraits and streetscapes

My mum is an artist and does fabulous portraits and sketches with pencil and needs a business card.
She likes designs that are a bit weird or unusual. The winning design will NOT be a slick modern corporate looking logo. It should be a little bit rustic and different. Interesting patterns and textures would be great, it doesn't even need to look like a business card! Come up with something unique!

Target Market(s)

Older clientele looking for family portraits

Industry/Entity Type

Artists

Contact Information for Business Card

Basically just need the name and contact details

Font styles to use
Decorative
Script

Requirements
Must have
• Lena Brodsworth
• Artist
• 0427913562
• lenabrodsworth@quillpost.example
Nice to have
• Weird artistic backgrounds, interesting textures, unusual designs for an artistic woman.
Should not have
• Nothing ultra modern and nothing corporate looking.

```html
<!DOCTYPE html>
<html lang="en">
<head>
<meta charset="utf-8">
<title>Lena Brodsworth – Artist Business Card</title>
<link rel="stylesheet" href="https://fonts.googleapis.com/css2?family=Courgette&display=swap">
<style>
  :root {
    --canvas-bg: #2e2f31;
    --ink-navy: #1f2488;
    --wash-mint: #9fe6d8;
    --wash-aqua: #8fd3d6;
    --wash-blue: #8fb7d8;
    --wash-lilac: #b3a4e3;
    --wash-violet: #9a86d6;
    --wash-pale: #eef0fb;
  }
  html, body {
    margin: 0;
    padding: 0;
    width: 1200px;
    height: 1027px;
    overflow: hidden;
    background: var(--canvas-bg);
  }
  .canvas {
    position: relative;
    width: 1200px;
    height: 1027px;
  }
  .card {
    position: absolute;
    width: 720px;
    height: 413px;
    overflow: hidden;
  }
  .card--front { left: 261px; top: 74px; }
  .card--back  { left: 111px; top: 535px; }

  .watercolour-wash {
    position: absolute;
    inset: 0;
  }
  .card--front .watercolour-wash {
    background:
      radial-gradient(ellipse 40% 45% at 12% 80%, var(--wash-pale) 0%, rgba(238,240,251,0) 100%),
      radial-gradient(ellipse 45% 40% at 35% 18%, var(--wash-mint) 0%, rgba(159,230,216,0) 100%),
      radial-gradient(ellipse 50% 55% at 85% 75%, var(--wash-violet) 0%, rgba(154,134,214,0) 100%),
      radial-gradient(ellipse 35% 35% at 80% 10%, var(--wash-lilac) 0%, rgba(179,164,227,0) 100%),
      linear-gradient(135deg, var(--wash-aqua) 0%, var(--wash-blue) 60%, var(--wash-lilac) 100%);
  }
  .card--back .watercolour-wash {
    background:
      radial-gradient(ellipse 45% 40% at 70% 20%, var(--wash-violet) 0%, rgba(154,134,214,0) 100%),
      radial-gradient(ellipse 30% 30% at 15% 20%, var(--wash-lilac) 0%, rgba(179,164,227,0) 100%),
      radial-gradient(ellipse 20% 15% at 35% 5%, var(--wash-pale) 0%, rgba(238,240,251,0) 100%),
      radial-gradient(ellipse 50% 40% at 30% 85%, var(--wash-aqua) 0%, rgba(143,211,214,0) 100%),
      linear-gradient(180deg, var(--wash-lilac) 0%, var(--wash-blue) 55%, var(--wash-aqua) 100%);
  }

  .card-text {
    position: absolute;
    left: 0;
    width: 100%;
    margin: 0;
    text-align: center;
    color: var(--ink-navy);
    font-family: "Courgette", cursive;
    white-space: nowrap;
    padding-left: 14px;
    box-sizing: border-box;
  }
  .artist-name {
    top: 146px;
    font-size: 36px;
    letter-spacing: 1px;
    font-weight: 400;
  }
  .artist-role {
    top: 199px;
    font-size: 19px;
  }
  .contact-line {
    font-size: 20px;
  }
  .contact-phone { top: 284px; }
  .contact-email { top: 313px; }
</style>
</head>
<body>
<main class="canvas">
  <section class="card card--front" aria-label="Business card front">
    <div class="watercolour-wash" role="img" aria-label="Mint, aqua and lilac watercolour wash background"></div>
    <h1 class="card-text artist-name">Lena Brodsworth</h1>
    <p class="card-text artist-role">Artist</p>
    <p class="card-text contact-line contact-phone">tel: 0427913562</p>
    <p class="card-text contact-line contact-email">mail: lenabrodsworth@quillpost.example</p>
  </section>

  <section class="card card--back" aria-label="Business card back">
    <div class="watercolour-wash" role="img" aria-label="Lilac, violet and pale blue watercolour wash background"></div>
  </section>
</main>
</body>
</html>
```